Tech House track needs a Cover design!

I need a CD Cover for an unreleased Tech House track. Please find attached a snipped of the song so you get an impression how it feels. I will also attach two existing covers which are already made for other tracks. I want to use kind of corporate design so it would be great if you design a cover which for example fits to the circle which is used in previous covers. Be creative in this. I will also provide my Logo so you can already place it on the cover. Name of the track is "Driftwood" which should also be found on the cover art.

Target Market(s)

Young people enjoying Tech House music on festivals or in a sunset session in their favourite venue.

Industry/Entity Type

Music Download

Colors

Designer to choose colors to be used in the design.

Requirements
Must have
• Circle kind of design. Including the logo and track title. Should fit electronic music!!
Nice to have
• can include kind of natural motives...maybe an implied sunset...
Should not have
• not too futuristic, no comic style,

```html
<!DOCTYPE html>
<html lang="en">
<head>
<meta charset="UTF-8">
<title>Driftwood – Cover</title>
<link rel="stylesheet" href="https://fonts.googleapis.com/css2?family=Exo+2:wght@500;700&display=swap">
<style>
  :root {
    --night: #15142b;
    --night-deep: #0d0c1e;
    --ember: #e08a22;
    --ember-glow: #f3b447;
    --magenta: #b23a78;
    --violet: #6a3a8a;
    --emblem-pink: rgba(216, 132, 230, 0.42);
    --emblem-lilac: rgba(169, 139, 232, 0.22);
    --text: #ffffff;
  }
  html, body {
    margin: 0;
    padding: 0;
    overflow: hidden;
    background: var(--night-deep);
  }
  .cover {
    position: relative;
    width: 1200px;
    height: 1200px;
    overflow: hidden;
    background: var(--night);
    font-family: "Exo 2", sans-serif;
  }
  .backdrop-photo {
    position: absolute;
    inset: 0;
    background:
      radial-gradient(ellipse 55% 45% at 10% 95%, var(--ember-glow) 0%, var(--ember) 30%, rgba(224,138,34,0) 75%),
      radial-gradient(ellipse 40% 50% at 40% 55%, rgba(190,100,40,0.5) 0%, rgba(190,100,40,0) 70%),
      radial-gradient(ellipse 35% 45% at 95% 45%, var(--magenta) 0%, rgba(178,58,120,0) 75%),
      radial-gradient(ellipse 40% 40% at 85% 90%, var(--violet) 0%, rgba(106,58,138,0) 75%),
      linear-gradient(160deg, var(--night-deep) 0%, var(--night) 60%, #241733 100%);
  }
  .emblem-art {
    position: absolute;
    left: 155px;
    top: 155px;
    width: 890px;
    height: 890px;
    border-radius: 50%;
    background: radial-gradient(circle at 50% 50%,
      rgba(0,0,0,0) 0%,
      var(--emblem-pink) 34%,
      rgba(0,0,0,0) 42%,
      var(--emblem-lilac) 70%,
      var(--emblem-pink) 88%,
      rgba(0,0,0,0) 100%);
  }
  .track-title {
    position: absolute;
    left: 82px;
    top: 72px;
    margin: 0;
    font-weight: 500;
    font-size: 60px;
    letter-spacing: 2px;
    line-height: 1;
    color: var(--text);
    text-transform: uppercase;
  }
  .label-name {
    position: absolute;
    right: 84px;
    bottom: 88px;
    margin: 0;
    font-weight: 700;
    font-size: 50px;
    letter-spacing: 3px;
    line-height: 1;
    color: var(--text);
    text-transform: uppercase;
  }
</style>
</head>
<body>
  <main class="cover">
    <div class="backdrop-photo" role="img" aria-label="Photograph of drifting smoke glowing orange at lower left and magenta at right on a dark night background, overlaid with fine diagonal stripes"></div>
    <div class="emblem-art" role="img" aria-label="Decorative emblem of concentric broken rings in pink and lilac, centred on the cover"></div>

    <h1 class="track-title">Driftwood</h1>
    <p class="label-name">Halcyon</p>
  </main>
</body>
</html>
```